BRC Business cards

We are a medium sized property company based in London and require a logo, Business card which reflects a professional company and incorporates our catchy name.

Our statement is (Building for the future) we like colours such as royal blue, greens and light browns but will look at anything.

Contact Information for Business Card

Brookcrest Estates Limited
Unit 4, 15-17 Farrowby Lane
London
SE22 7QN

Web: www.brookcrestestates-example.com

Email: brookcrestltd@mailbox-example.com

Telephone: +44-208-555-0142
Fax: +44-208-555-0187

```html
<!DOCTYPE html>
<html lang="en">
<head>
<meta charset="utf-8">
<title>Brookcrest Estates Limited – Business Card</title>
<link rel="stylesheet" href="https://fonts.googleapis.com/css2?family=Comfortaa:wght@300&family=Exo+2:wght@500;700&display=swap">
<style>
  :root {
    --card-black: #000000;
    --lime: #a4f03c;
    --lime-deep: #7fcc22;
    --silver: #c9ccc9;
    --white: #f4f4f4;
  }
  html, body {
    margin: 0;
    padding: 0;
    width: 1200px;
    height: 791px;
    overflow: hidden;
    background: var(--card-black);
  }
  .business-card {
    position: relative;
    width: 1200px;
    height: 791px;
    background: var(--card-black);
    overflow: hidden;
  }
  .logo-mark-area {
    position: absolute;
    left: 350px;
    top: 88px;
    width: 480px;
    height: 262px;
    background: linear-gradient(180deg, var(--lime) 0%, var(--lime-deep) 100%);
  }
  .brand-name {
    position: absolute;
    top: 378px;
    left: 0;
    width: 1200px;
    margin: 0;
    text-align: center;
    font-family: "Comfortaa", sans-serif;
    font-weight: 300;
    font-size: 60px;
    letter-spacing: 1px;
    color: var(--silver);
    line-height: 1;
    white-space: nowrap;
  }
  .contact-list {
    position: absolute;
    left: 36px;
    top: 488px;
    margin: 0;
    padding: 0;
    list-style: none;
    font-family: "Exo 2", sans-serif;
    font-weight: 500;
    font-size: 29px;
    color: var(--white);
  }
  .contact-item {
    display: flex;
    align-items: center;
    height: 34px;
    margin-bottom: 22px;
    white-space: nowrap;
  }
  .contact-item.is-tight { margin-bottom: 18px; }
  .contact-icon {
    flex: none;
    width: 32px;
    height: 32px;
    margin-right: 26px;
  }
  .accent { color: var(--lime); }
  .footer-band-silver {
    position: absolute;
    left: 0;
    top: 751px;
    width: 1200px;
    height: 11px;
    background: var(--silver);
  }
  .footer-band-lime {
    position: absolute;
    left: 0;
    top: 762px;
    width: 1200px;
    height: 29px;
    background: var(--lime);
  }
  .icon-disc { fill: var(--lime); }
  .icon-letter {
    font-family: "Exo 2", sans-serif;
    font-weight: 700;
    font-size: 19px;
    fill: var(--card-black);
  }
</style>
</head>
<body>
<main class="business-card">
  <div class="logo-mark-area" role="img" aria-label="Company mark area for Brookcrest Estates"></div>

  <h1 class="brand-name">brookcrest estates ltd</h1>

  <ul class="contact-list">
    <li class="contact-item">
      <svg class="contact-icon" viewBox="0 0 32 32" aria-hidden="true"><circle class="icon-disc" cx="16" cy="16" r="15"/><text class="icon-letter" x="16" y="23" text-anchor="middle">A</text></svg>
      <span>Unit 4<span class="accent">,</span> 15 <span class="accent">–</span> 17 Farrowby Lane<span class="accent">,</span> London, SE22 7QN</span>
    </li>
    <li class="contact-item">
      <svg class="contact-icon" viewBox="0 0 32 32" aria-hidden="true"><circle class="icon-disc" cx="16" cy="16" r="15"/><text class="icon-letter" x="16" y="23" text-anchor="middle">T</text></svg>
      <span>+44 <span class="accent">.</span> 208 <span class="accent">.</span> 555 <span class="accent">.</span> 0142</span>
    </li>
    <li class="contact-item is-tight">
      <svg class="contact-icon" viewBox="0 0 32 32" aria-hidden="true"><circle class="icon-disc" cx="16" cy="16" r="15"/><text class="icon-letter" x="16" y="23" text-anchor="middle">F</text></svg>
      <span>+44 <span class="accent">.</span> 208 <span class="accent">.</span> 555 <span class="accent">.</span> 0187</span>
    </li>
    <li class="contact-item is-tight">
      <svg class="contact-icon" viewBox="0 0 32 32" aria-hidden="true"><circle class="icon-disc" cx="16" cy="16" r="15"/><text class="icon-letter" x="16" y="23" text-anchor="middle">E</text></svg>
      <span>brookcrestltd@mailbox-example.com</span>
    </li>
    <li class="contact-item">
      <svg class="contact-icon" viewBox="0 0 32 32" aria-hidden="true"><circle class="icon-disc" cx="16" cy="16" r="15"/><text class="icon-letter" x="16" y="23" text-anchor="middle">W</text></svg>
      <span>brookcrestestates-example.com</span>
    </li>
  </ul>

  <div class="footer-band-silver"></div>
  <div class="footer-band-lime"></div>
</main>
</body>
</html>
```